Business Cards

We are an innovating group of real estate investors who buy beat up house's, fix them up, and resell them. We are in need of a business card that is catchy and stands out. We want it to say something like " We buy house's cash fast" Call us first

Industry/Entity Type

Business

Requirements
Must have
• Our logo which is updated

```html
<!DOCTYPE html>
<html lang="en">
<head>
<meta charset="utf-8">
<title>Brisk Gable Real Estate Investors – Business Card</title>
<link rel="stylesheet" href="https://fonts.googleapis.com/css2?family=Arimo:wght@400;700&family=Didact+Gothic&display=swap">
<style>
  :root {
    --page: #e9e7e3;
    --ink: #111111;
    --card-black: #0b0b0b;
    --card-black-soft: #222222;
    --paper: #ffffff;
    --purple: #8e2b8f;
    --magenta: #b0399f;
    --green: #6cb33f;
    --green-bright: #7cc242;
    --text-light: #f2f2f2;
  }
  * { margin: 0; padding: 0; box-sizing: border-box; }
  html, body { width: 1200px; height: 784px; overflow: hidden; }
  body {
    background: var(--page);
    font-family: "Arimo", Arial, sans-serif;
    display: flex;
    align-items: center;
    justify-content: center;
    gap: 40px;
  }
  .card {
    width: 540px;
    height: 310px;
    position: relative;
    overflow: hidden;
    box-shadow: 0 6px 18px rgba(0,0,0,0.25);
  }

  /* Back side */
  .card-back {
    background: radial-gradient(ellipse at 50% 40%, var(--card-black-soft) 0%, var(--card-black) 70%);
  }
  .card-back .tagline {
    position: absolute;
    left: 0; right: 0;
    top: 138px;
    text-align: center;
    font-family: "Didact Gothic", "Century Gothic", sans-serif;
    font-size: 15px;
    letter-spacing: 3px;
    white-space: nowrap;
  }
  .tagline .quote { color: var(--magenta); }
  .tagline .call { color: var(--green-bright); }

  /* Front side */
  .card-front { background: var(--paper); }
  .card-front .lower-panel {
    position: absolute; left: 0; right: 0; top: 168px; bottom: 0;
    background: var(--card-black);
    border-top: 7px solid var(--green);
  }
  .person {
    position: absolute; right: 26px; top: 18px; text-align: right;
  }
  .person .name { color: var(--purple); font-size: 13px; }
  .person .role { color: var(--ink); font-size: 11px; margin-top: 3px; }

  .brand {
    position: absolute; left: 44px; top: 74px;
    display: flex; align-items: center; gap: 14px;
  }
  .brand .mark {
    width: 64px; height: 64px; background: var(--purple);
  }
  .brand .name {
    font-weight: 700; font-size: 30px; color: var(--purple); line-height: 1;
  }
  .brand .descriptor {
    font-weight: 700; font-size: 11.5px; color: var(--ink);
    letter-spacing: 0.4px; margin-top: 4px;
  }

  .contacts {
    position: absolute; left: 40px; top: 190px;
    list-style: none; color: var(--text-light);
    font-size: 15px; line-height: 21px;
  }
  .contacts li { display: flex; align-items: flex-start; gap: 8px; }
  .contacts svg { width: 15px; height: 15px; margin-top: 3px; flex: none; fill: var(--purple); }
</style>
</head>
<body>

  <section class="card card-back" aria-label="Card back">
    <p class="tagline"><span class="quote">"We buy house's cash fast"</span> <span class="call">Call us first</span></p>
  </section>

  <section class="card card-front" aria-label="Card front">
    <div class="person">
      <p class="name">Dana Hollis</p>
      <p class="role">Manager</p>
    </div>

    <div class="lower-panel"></div>

    <div class="brand">
      <div class="mark"></div>
      <div>
        <p class="name">Brisk Gable</p>
        <p class="descriptor">REAL ESTATE INVESTORS</p>
      </div>
    </div>

    <ul class="contacts">
      <li>
        <svg viewBox="0 0 16 16" aria-hidden="true"><path d="M3.5 1.5l2.5 0 1 3.5-1.6 1.2a8 8 0 0 0 4.4 4.4L11 9l3.5 1v2.5c0 1-1 2-2 2A11 11 0 0 1 1.5 3.5c0-1 1-2 2-2z"/></svg>
        <span>0400 123 456</span>
      </li>
      <li>
        <svg viewBox="0 0 16 16" aria-hidden="true"><path d="M8 1a7 7 0 1 0 0 14A7 7 0 0 0 8 1zm0 1.5c.8 0 1.8 1.6 2.1 4.5H5.9C6.2 4.1 7.2 2.5 8 2.5zM2.6 7a5.5 5.5 0 0 1 2.6-4c-.5 1-.8 2.4-.9 4H2.6zm0 2h1.7c.1 1.6.4 3 .9 4a5.5 5.5 0 0 1-2.6-4zM8 13.5c-.8 0-1.8-1.6-2.1-4.5h4.2c-.3 2.9-1.3 4.5-2.1 4.5zm2.8-.5c.5-1 .8-2.4.9-4h1.7a5.5 5.5 0 0 1-2.6 4zm.9-6c-.1-1.6-.4-3-.9-4a5.5 5.5 0 0 1 2.6 4h-1.7z"/></svg>
        <span>www.briskgable.com</span>
      </li>
      <li>
        <svg viewBox="0 0 16 16" aria-hidden="true"><path d="M1 3h14v10H1V3zm1.5 1.5v.4L8 9l5.5-4.1v-.4h-11zm11 2.3L8 11 2.5 6.8v4.7h11V6.8z"/></svg>
        <span>dana@briskgable.com</span>
      </li>
      <li>
        <svg viewBox="0 0 16 16" aria-hidden="true"><path d="M8 1.5L1 8h2v6.5h4v-4h2v4h4V8h2L8 1.5z"/></svg>
        <span>Shop 4 Harbour Plaza, 118 Coastline<br>Drive Seacliff NSW 2500</span>
      </li>
    </ul>
  </section>

</body>
</html>
```